Logo+Business Card Design for Architecture Photographer

Hi Everyone,

I am looking for logo/business designs for my new business - Brovald Studio. My business does commercial photography with a specialization in architecture, luxury real estate, and design. The Int is short for interior and ex is short for exterior.

Some of the values of my business are:
- providing top quality photography and post-processing (straight lines, accurate and bold whites/blacks/colors) for commercial use (websites, social media, advertising campaigns)
- fostering a collaborative workflow that is professional and fun that will have clients returning because of the premium service they received
- asking the right questions so that I can capture what matters to my clients with my own creative vision

I want my final look to be modern and bold. The business cards will be letter pressed/debossed, so the design should incorporate that. I am imagining a solid matte olive green or matte navy blue background on one side and white on the other. The card will be printed on colored cards, so you don't have to put a colored background as part of the design. I have attached some examples of colors I like, although it doesn't matter too much for the purpose of your work.

I want the debossing to be part of the design of the business card. This debossing should be some some of pattern or a frame that holds the logo on the back of the card (I have attached some sample images named geometric debossing to show what I mean). Then I can just foil print my logo on the back. My contact info and a logo will be on the front.

Somewhere it should say "Architecture, Luxury Real Estate, Design".

My vision for the logo: no cameras or buildings. I can't think of anything symbolic for the logo, but it should somehow contain Brovald. It might be cool to have them separated by a line like Bro | Vald. Or have the Int inside something, and the Ex outside.

I plan on using Quelmark to print the cards. You can find their specifications here: https://quelmark.example/products/duplex-business-cards?variant=4837201956372

It would be nice to have a psd file that I can edit as well as a PDF to deliver to the printing company. Both must be vector graphics.

Thank you to everyone who has submitted a design as it has helped me get a better idea of what I want.

Target Market(s)

Designers, architects

Industry/Entity Type

Photographer

Contact Information for Business Card

See project description

Logo Text

Brovald Studio

Font styles to use
Sans Serif
Decorative

Colors
ffffff

Requirements
Must have
• Logo and business card design. Deboss area less than 3 square inches. Deboss area should be some sort of a pattern/design as shown in attachments labelled "Geometric Debossing Example".
• Logo design and deboss design must be submitted in vector graphics.
Nice to have
• Color doesn't have to be shown on the design because I will be printing on colored paper, although it would be helpful to help me visualize what it will eventually look like.
Should not have
• A camera or building in the design...too cliche.

```html
<!DOCTYPE html>
<html lang="en">
<head>
<meta charset="utf-8">
<title>Brovald Studio – Business Card</title>
<link href="https://fonts.googleapis.com/css2?family=Montserrat:wght@500;700&family=Roboto:wght@400;500;700&display=swap" rel="stylesheet">
<style>
  :root {
    --stage: #2b2b30;
    --card-dark: #1c1b1e;
    --deboss: #161518;
    --card-light: #fbfbfb;
    --ink: #1a1a1a;
    --accent: #2ea3e3;
    --muted: #444;
  }
  html, body {
    margin: 0;
    width: 1200px;
    height: 800px;
    overflow: hidden;
    background: var(--stage);
  }
  .canvas {
    position: relative;
    width: 1200px;
    height: 800px;
  }
  .card {
    position: absolute;
    top: 245px;
    width: 540px;
    height: 309px;
    border-radius: 3px;
    box-shadow: 0 14px 30px rgba(0,0,0,.45);
    overflow: hidden;
  }
  .card-back {
    left: 40px;
    background: var(--card-dark);
  }
  .card-front {
    left: 620px;
    background: var(--card-light);
  }
  .deboss-area {
    position: absolute;
    left: 40px;
    top: 40px;
    width: 230px;
    height: 230px;
    border-radius: 50%;
    background: radial-gradient(circle at 45% 40%, #1f1e21, var(--deboss));
    box-shadow: inset 2px 2px 4px rgba(0,0,0,.6), inset -1px -1px 2px rgba(255,255,255,.04);
  }
  .wordmark {
    position: absolute;
    display: flex;
    align-items: center;
    gap: 10px;
    font-family: "Montserrat", sans-serif;
    font-weight: 700;
    white-space: nowrap;
  }
  .wordmark-dot {
    width: 22px;
    height: 22px;
    border-radius: 50%;
    background: var(--accent);
  }
  .card-back .wordmark {
    right: 36px;
    top: 130px;
    font-size: 30px;
    color: #ffffff;
  }
  .card-front .wordmark {
    left: 34px;
    top: 178px;
    font-size: 26px;
    color: var(--ink);
  }
  .divider {
    position: absolute;
    left: 292px;
    top: 70px;
    width: 1px;
    height: 150px;
    background: var(--accent);
    opacity: .7;
  }
  .contact {
    position: absolute;
    left: 312px;
    top: 74px;
    font-family: "Roboto", sans-serif;
    color: var(--ink);
  }
  .contact-name {
    margin: 0;
    font-size: 19px;
    font-weight: 700;
  }
  .contact-role {
    margin: 0 0 10px;
    font-size: 13px;
    color: var(--accent);
  }
  .contact-line {
    margin: 0;
    font-size: 11.5px;
    line-height: 17px;
    color: var(--muted);
    display: flex;
    align-items: center;
    gap: 6px;
  }
  .contact-line svg {
    width: 10px;
    height: 10px;
    fill: var(--accent);
    flex: none;
  }
  .contact-address { margin-bottom: 4px; }
  .web-accent { color: var(--accent); }
</style>
</head>
<body>
<main class="canvas">
  <section class="card card-back" aria-label="Card back">
    <div class="deboss-area" role="img" aria-label="Debossed geometric pattern area"></div>
    <div class="wordmark"><span class="wordmark-dot"></span>Brovald Studio</div>
  </section>

  <section class="card card-front" aria-label="Card front">
    <div class="wordmark"><span class="wordmark-dot"></span>Brovald Studio</div>
    <div class="divider"></div>
    <div class="contact">
      <p class="contact-name">Dana Whitlow</p>
      <p class="contact-role">President</p>
      <div class="contact-address">
        <p class="contact-line">PO BOX 418 Harbor Lane</p>
        <p class="contact-line">14 Fenwick Row Eastvale</p>
      </div>
      <p class="contact-line">
        <svg viewBox="0 0 10 10" aria-hidden="true"><path d="M2 0.5 L3.8 2.5 L3 3.6 Q4 5.8 6.4 7 L7.5 6.2 L9.5 8 L8.4 9.5 Q3.5 9 0.5 1.6 Z"/></svg>
        555-014-2290
      </p>
      <p class="contact-line">
        <svg viewBox="0 0 10 10" aria-hidden="true"><path d="M0 2 H10 V8 H0 Z M0.6 2.4 L5 5.6 L9.4 2.4" stroke="#fff" stroke-width="0.7"/></svg>
        hello@brovaldstudio.example
      </p>
      <p class="contact-line">
        <svg viewBox="0 0 10 10" aria-hidden="true"><circle cx="5" cy="5" r="4.6"/></svg>
        www.<span class="web-accent">brovaldstudio</span>.example
      </p>
    </div>
  </section>
</main>
</body>
</html>
```